Plastic Pots, Hanging Baskets, and Plastic Tray Manufacturer Catalog

Catalog design for a newer company looking for a fresh take on plastics offerings, need layout design but attached some ideas in the project

Industry/Entity Type

It Company

Colors
a2cd3a
cadf82
eaf2ce

```html
<!DOCTYPE html>
<html lang="en">
<head>
<meta charset="utf-8">
<title>Greenfold USA Corp – Catalog Spread</title>
<link href="https://fonts.googleapis.com/css2?family=Montserrat:wght@600;700;800&family=Lato:wght@400;700&family=Merienda:wght@400&display=swap" rel="stylesheet">
<style>
  :root{
    --green:#a2cd3a;
    --green-mid:#b6d75c;
    --green-light:#cadf82;
    --green-pale:#eaf2ce;
    --ink:#1e1e1e;
    --slab:#222222;
    --paper:#ffffff;
    --paper-shade:#ededed;
    --stage:#e4e4e4;
    --text:#2b2b2b;
  }
  *{box-sizing:border-box;margin:0;padding:0}
  html,body{width:1200px;height:900px;overflow:hidden;background:var(--stage)}
  .spread{position:absolute;left:40px;top:50px;width:1120px;height:800px;background:var(--paper);box-shadow:0 6px 24px rgba(0,0,0,.18)}
  .bands{position:absolute;inset:0}
  .page{position:absolute;top:0;width:560px;height:800px}
  .page--back{left:0;background:linear-gradient(90deg,var(--paper) 85%,var(--paper-shade))}
  .page--cover{left:560px;background:linear-gradient(90deg,var(--paper-shade),var(--paper) 15%)}
  .page--overlay{background:none}
  .photo{position:absolute}
  .photo--building{left:290px;top:100px;width:270px;height:330px;background:linear-gradient(160deg,#cfe0ec 0%,#e8e8e4 35%,#bfc4c0 70%,#7e9a5e 100%)}
  .photo--seedlings{left:0;top:90px;width:560px;height:270px;background:linear-gradient(120deg,#3a2a1e 0%,#4f6b2a 35%,#7ccf4a 60%,#d6ef7a 85%,#eef6d8 100%)}
  .about{position:absolute;left:0;top:100px;width:290px}
  .about__title{background:linear-gradient(90deg,var(--green),var(--green-light));padding:8px 20px;font:700 22px 'Montserrat',sans-serif;color:var(--ink)}
  .about__text{padding:14px 18px 0 20px;font:400 10.5px/1.5 'Lato',sans-serif;color:var(--text);text-align:justify}
  .brand{display:flex;align-items:center;gap:10px}
  .brand__mark{width:14px;height:14px;background:var(--green);flex:none}
  .brand__name{font:800 14px 'Montserrat',sans-serif;color:var(--ink);letter-spacing:.5px;white-space:nowrap}
  .brand__tagline{font:400 11px 'Merienda',cursive;color:var(--ink);white-space:nowrap}
  .about__brand{position:absolute;left:60px;top:386px}
  .about__brand .brand__tagline{margin:2px 0 0 24px}
  .contact{position:absolute;left:0;width:560px;top:580px;text-align:center;color:var(--ink)}
  .contact__title{font:700 24px 'Montserrat',sans-serif;margin-bottom:10px}
  .contact__list{list-style:none;font:400 12.5px/1.55 'Lato',sans-serif}
  .contact__list svg{width:10px;height:10px;vertical-align:-1px;margin-right:5px;fill:var(--ink)}
  .cover__brand{position:absolute;left:110px;top:476px}
  .cover__brand .brand__mark{width:38px;height:38px}
  .cover__brand .brand__name{font-size:24px}
  .cover__brand .brand__tagline{font-size:15px;margin:4px 0 0 48px}
  .cover__web{position:absolute;left:0;width:560px;top:639px;text-align:center;font:400 11px 'Lato',sans-serif;color:var(--paper)}
</style>
</head>
<body>
<main class="spread">
  <section class="page page--back">
    <div class="photo photo--building" role="img" aria-label="Photo of the company office building"></div>
  </section>
  <section class="page page--cover">
    <div class="photo photo--seedlings" role="img" aria-label="Photo of seedlings growing in plastic trays and pots with a spray bottle"></div>
  </section>

  <svg class="bands" viewBox="0 0 1120 800" aria-hidden="true">
    <path d="M0 470 L430 430 Q500 420 560 410 L560 445 Q470 455 420 465 L0 500 Z" fill="var(--green-light)"/>
    <path d="M0 500 L420 468 L440 500 L0 540 Z" fill="var(--green)"/>
    <rect x="0" y="510" width="80" height="40" fill="var(--slab)"/>
    <path d="M0 560 L440 515 L420 545 L0 590 Z" fill="var(--green)"/>
    <path d="M440 440 L560 430 L560 540 L480 540 Z" fill="var(--slab)"/>
    <rect x="560" y="55" width="560" height="35" fill="var(--green)"/>
    <path d="M560 360 Q820 390 1120 375 L1120 410 Q820 420 560 405 Z" fill="var(--green-light)"/>
    <path d="M560 410 L660 415 L640 545 L560 545 Z" fill="var(--slab)"/>
    <path d="M700 430 L1120 418 L1120 450 L700 465 Z" fill="var(--green)"/>
    <rect x="1055" y="335" width="65" height="40" fill="var(--slab)"/>
    <path d="M560 592 L1120 552 L1120 584 L560 624 Z" fill="var(--slab)"/>
    <rect x="560" y="630" width="560" height="32" fill="var(--slab)"/>
  </svg>

  <section class="page page--back page--overlay">
    <div class="about">
      <h2 class="about__title">About Us</h2>
      <p class="about__text">Greenfold USA Corp was founded in sunny Fresno, California. During tough economic times, we have recognized the horticultural industry needs to reduce production costs, and our company has been built on filling that market need. Because many of our customers were unfamiliar with working overseas, Greenfold USA was formed to bridge the gap between an overseas company to the US. We're here to help our clients connect to product 10-30% below what they have been paying, while maintaining the industry high quality requirements. Furthermore, we are here to facilitate shipments, and will handle all customs, freight, and shipping for you, to make overseas orders easier than ever.</p>
    </div>
    <div class="about__brand">
      <div class="brand"><span class="brand__mark"></span><span class="brand__name">GREENFOLD USA CORP</span></div>
      <p class="brand__tagline">For all your horticultural needs</p>
    </div>
    <div class="contact">
      <h2 class="contact__title">Contact Us</h2>
      <ul class="contact__list">
        <li><svg viewBox="0 0 10 10"><path d="M5 0a3.5 3.5 0 0 0-3.5 3.5C1.5 6 5 10 5 10s3.5-4 3.5-6.5A3.5 3.5 0 0 0 5 0zm0 5a1.5 1.5 0 1 1 0-3 1.5 1.5 0 0 1 0 3z"/></svg>1450 W. Orchard Ave, Suite 120,<br>Fresno, CA 93711</li>
        <li><svg viewBox="0 0 10 10"><path d="M2 0l2 2.5-1 1.2a6 6 0 0 0 3.3 3.3l1.2-1L10 8l-1.5 2C4 10 0 6 0 1.5z"/></svg>(555)014 2000</li>
        <li><svg viewBox="0 0 10 10"><path d="M2 0h6v3H2zM0 3.5h10V8H8v2H2V8H0zM3 7v2h4V7z"/></svg>(555)014 2003</li>
        <li><svg viewBox="0 0 10 10"><path d="M0 2h10v6H0zm1 1l4 3 4-3z"/></svg>info@greenfoldusa.com</li>
        <li><svg viewBox="0 0 10 10"><circle cx="5" cy="5" r="4.5"/></svg>www.greenfoldusa.com</li>
      </ul>
    </div>
  </section>

  <section class="page page--cover page--overlay">
    <div class="cover__brand">
      <div class="brand"><span class="brand__mark"></span><span class="brand__name">GREENFOLD USA CORP</span></div>
      <p class="brand__tagline">For all your horticultural needs</p>
    </div>
    <p class="cover__web">www.greenfoldusa.com</p>
  </section>
</main>
</body>
</html>
```